Fast Growing Personal Injury Law Firm Needs Business Card Design

We need a business card design for a fast growing personal injury law firm in Florida. Our name is Darren Kolvisty, P.A. Our practice is comprised of younger attorneys (in their 30s) that employ more modern techniques/tools than our older competition. We would prefer a look that is a modern play on a classic look. Also, we would like to continue using a color scheme that employs navy blue and kelly green (other shades of green could be fine too) as well as our "E" logo.

Industry/Entity Type

Law Firm

```html
<!DOCTYPE html>
<html lang="en">
<head>
<meta charset="utf-8">
<title>Darren Kolvisty, P.A. — Stationery</title>
<link rel="stylesheet" href="https://fonts.googleapis.com/css2?family=Figtree:wght@400;600&family=Open+Sans:wght@400&display=swap">
<style>
:root{
  --navy:#1f3060;
  --green:#0f7a3a;
  --board:#8a8a8a;
  --paper:#ffffff;
  --ghost:#e6e6e8;
  --rule:#9aa3b8;
  --ink:#222;
}
*{margin:0;padding:0;box-sizing:border-box}
html,body{width:1200px;height:640px;overflow:hidden;background:var(--board)}
body{position:relative;font-family:"Figtree",sans-serif;color:var(--navy)}
.sheet{position:absolute;background:var(--paper);overflow:hidden;box-shadow:3px 4px 6px rgba(0,0,0,.35)}
.mark{display:inline-block;background:var(--green);border:2px solid var(--navy)}
.firm{font-weight:400;color:var(--navy);line-height:1.1}
.tagline{font-weight:600;color:var(--green);line-height:1.1}
.name{font-weight:600;color:var(--green);line-height:1.1}
.role{font-size:6px;color:var(--navy)}
.contact{font-size:7px;line-height:1.45;color:var(--navy)}
.contact li{list-style:none;display:flex;align-items:center;gap:4px}
.contact svg{width:6px;height:6px;fill:currentColor}
.gap{height:5px}
.ghost-name{position:absolute;font-family:"Figtree",sans-serif;font-weight:400;color:var(--ghost);white-space:nowrap;line-height:1}

/* letterhead */
.letterhead{left:34px;top:72px;width:385px;height:497px;border-top:4px solid var(--navy)}
.letterhead .brand{position:absolute;left:28px;top:22px;display:flex;align-items:center;gap:7px}
.letterhead .mark{width:33px;height:33px}
.letterhead .firm{font-size:14px}
.letterhead .tagline{font-size:9px}
.letterhead .contact{position:absolute;left:289px;top:18px;font-size:4.6px;line-height:1.35}
.letterhead .contact svg{width:4px;height:4px}
.letter{position:absolute;left:29px;top:106px;width:330px;font-family:"Open Sans",sans-serif;font-size:6.2px;line-height:13.6px;color:var(--ink)}
.letter p{margin-bottom:9px}
.signature{width:92px;height:30px;margin:2px 0 8px;background:linear-gradient(90deg,#fff,#d8d8d8,#fff)}
.letterhead .ghost-name{right:14px;bottom:16px;font-size:56px}

/* business cards */
.card{width:221px;height:126px}
.card .name{font-size:9px}
.card .contact{position:absolute}
.c1{left:453px;top:88px;background:var(--navy)}
.c1 .head{position:absolute;right:10px;top:11px;text-align:right;color:#fff}
.c1 .head .name{color:#fff}
.c1 .head .role{color:#fff}
.c1 .contact{left:18px;top:56px;color:#fff}
.c1 .ghost-name{right:10px;top:40px;font-size:26px;color:rgba(255,255,255,.14)}

.c2{left:696px;top:88px}
.c2 .mark{position:absolute;left:17px;top:11px;width:31px;height:31px}
.c2 .head{position:absolute;right:12px;top:11px;text-align:right}
.c2 .contact{left:17px;top:70px}

.c3{left:939px;top:88px}
.c3 .brand{position:absolute;left:17px;top:12px;display:flex;align-items:center;gap:5px}
.c3 .mark{width:24px;height:24px}
.c3 .firm{font-size:10.5px}
.c3 .tagline{font-size:7px}
.c3 .who{position:absolute;left:16px;top:50px}
.c3 .contact{left:106px;top:38px}
.c3 .band{position:absolute;left:0;bottom:0;width:100%;height:11px;background:var(--navy)}
.c3 .band::before{content:"";position:absolute;left:0;top:0;width:132px;height:11px;background:var(--green);clip-path:polygon(0 0,100% 0,95% 100%,0 100%)}
.c3 .web{position:absolute;right:14px;bottom:1px;font-size:6.5px;color:#fff;display:flex;align-items:center;gap:3px}
.c3 .web svg{width:6px;height:6px;fill:#fff}

.c4{left:453px;top:246px;text-align:center}
.c4 .mark{position:absolute;left:79px;top:20px;width:63px;height:54px}
.c4 .firm{position:absolute;left:0;right:0;top:82px;font-size:15.5px}
.c4 .tagline{position:absolute;left:0;right:0;top:101px;font-size:10px}

.c5{left:696px;top:246px}
.c6{left:939px;top:246px}
.c5 .head,.c6 .head{position:absolute;right:14px;top:18px;text-align:right}
.c5 .line,.c6 .line{position:absolute;left:0;top:36px;width:168px;height:1px;background:var(--rule)}
.c5 .contact,.c6 .contact{left:14px;top:49px}
.c5 .mark{position:absolute;right:14px;top:74px;width:45px;height:36px}
.c6 .ghost-name{right:10px;top:44px;font-size:24px}

/* envelopes */
.envelope{width:349px;height:159px}
.e1{left:453px;top:410px}
.e1 .brand{position:absolute;left:20px;top:17px;display:flex;align-items:center;gap:5px}
.e1 .mark{width:18px;height:18px}
.e1 .firm{font-size:7.5px}
.e1 .tagline{font-size:5px}
.e1 .contact{position:absolute;left:20px;top:42px;font-size:4.2px;line-height:1.4}
.e1 .contact svg{width:3.5px;height:3.5px}
.e1 .ghost-name{right:14px;bottom:16px;font-size:46px}
.e2{left:823px;top:410px}
.e2 svg.flap{position:absolute;left:0;top:0;width:349px;height:40px}
.e2 .mark{position:absolute;left:161px;top:6px;width:27px;height:25px}
</style>
</head>
<body>
<svg width="0" height="0" style="position:absolute" aria-hidden="true">
  <symbol id="i-phone" viewBox="0 0 10 10"><path d="M2 1h2l1 2-1.2 1a6 6 0 0 0 2.2 2.2L7 5l2 1v2c0 .6-.4 1-1 1A8 8 0 0 1 1 2c0-.6.4-1 1-1z"/></symbol>
  <symbol id="i-fax" viewBox="0 0 10 10"><path d="M3 1h4v3H3zM1 4h8v5H1zm2 2v1h1V6zm3 0v1h1V6z"/></symbol>
  <symbol id="i-mail" viewBox="0 0 10 10"><path d="M1 2h8v6H1zm1 1 3 2.2L8 3z"/></symbol>
  <symbol id="i-web" viewBox="0 0 10 10"><path d="M5 1a4 4 0 1 0 0 8A4 4 0 0 0 5 1zm0 1.2c.6.6 1 1.6 1.1 2.3H3.9C4 3.8 4.4 2.8 5 2.2zM2.3 5.5h1.6c.1.8.5 1.7 1.1 2.3a3 3 0 0 1-2.7-2.3zm3.7 2.3c.6-.6 1-1.5 1.1-2.3h1.6A3 3 0 0 1 6 7.8z"/></symbol>
</svg>

<section class="sheet letterhead">
  <div class="ghost-name">Kolvisty</div>
  <div class="brand">
    <span class="mark"></span>
    <div><div class="firm">Darren Kolvisty, P.A.</div><div class="tagline">Personal Injury Attorneys</div></div>
  </div>
  <ul class="contact">
    <li><svg><use href="#i-phone"/></svg>941.555.0182</li>
    <li><svg><use href="#i-fax"/></svg>941.555.0147</li>
    <li><svg><use href="#i-mail"/></svg>darren@kolvistylaw.com</li>
    <li><svg><use href="#i-web"/></svg>kolvistylaw.com</li>
    <li>2150 Harbor Point Drive Suite 410</li>
    <li>Bayview Ranch, Florida 34299</li>
  </ul>
  <div class="letter">
    <p>Lorem Ipsum is simply</p>
    <p>dummy text of the printing and typesetting industry. Lorem Ipsum has been the industry's standard dummy text ever since the 1500s, when an unknown printer took a galley of type and scrambled it to make a type specimen book. It has survived not only five centuries, but also the leap into electronic typesetting, remaining essentially unchanged. It was popularised in the 1960s with the release of Presstype sheets containing Lorem Ipsum passages, and more recently with desktop publishing software like PageSetter Pro including versions of Lorem Ipsum.</p>
    <p>It is a long established fact that a reader will be distracted by the readable content of a page when looking at its layout. The point of using Lorem Ipsum is that it has a more-or-less normal distribution of letters, as opposed to using 'Content here, content here', making it look like readable English. Many desktop publishing packages and web page editors now use Lorem Ipsum as their default model text, and a search for 'lorem ipsum' will uncover many web sites still in their infancy. Various versions have evolved over the years, sometimes by accident, sometimes on purpose (injected humour and the like).</p>
    <p>Contrary to popular belief, Lorem Ipsum is not simply random text. It has roots in a piece of classical Latin literature from 45 BC, making it over 2000 years old. A Latin professor looked up one of the more obscure Latin words, consectetur, from a Lorem Ipsum passage, and going through the cites of the word in classical literature, discovered the undoubtable source. Lorem Ipsum comes from sections 1.10.32 and 1.10.33 of "Tractatus de Finibus" (The Extremes of Good and Evil) by an ancient orator, written in 45 BC. This book</p>
    <p style="margin-bottom:0">Lorem Ipsum</p>
    <div class="signature" role="img" aria-label="Handwritten signature"></div>
    <p>Lorem Ipsum is a dummy</p>
  </div>
</section>

<section class="sheet card c1">
  <div class="ghost-name">Kolvisty</div>
  <div class="head"><div class="name">Darren Kolvisty</div><div class="role">Attorney at Law</div></div>
  <ul class="contact">
    <li><svg><use href="#i-phone"/></svg>941.555.0182</li>
    <li><svg><use href="#i-fax"/></svg>941.555.0147</li>
    <li class="gap"></li>
    <li><svg><use href="#i-mail"/></svg>darren@kolvistylaw.com</li>
    <li><svg><use href="#i-web"/></svg>kolvistylaw.com</li>
    <li class="gap"></li>
    <li>2150 Harbor Point Drive Suite 410</li>
    <li>Bayview Ranch, Florida 34299</li>
  </ul>
</section>

<section class="sheet card c2">
  <span class="mark"></span>
  <div class="head"><div class="name">Darren Kolvisty</div><div class="role">Attorney at Law</div></div>
  <ul class="contact">
    <li><svg><use href="#i-phone"/></svg>941.555.0182</li>
    <li><svg><use href="#i-fax"/></svg>941.555.0147</li>
    <li><svg><use href="#i-mail"/></svg>darren@kolvistylaw.com</li>
    <li>2150 Harbor Point Drive Suite 410</li>
    <li>Bayview Ranch, Florida 34299</li>
  </ul>
</section>

<section class="sheet card c3">
  <div class="brand">
    <span class="mark"></span>
    <div><div class="firm">Darren Kolvisty, P.A.</div><div class="tagline">Personal Injury Attorneys</div></div>
  </div>
  <div class="who"><div class="name">Darren Kolvisty</div><div class="role">Attorney at Law</div></div>
  <ul class="contact">
    <li><svg><use href="#i-phone"/></svg>941.555.0182</li>
    <li><svg><use href="#i-fax"/></svg>941.555.0147</li>
    <li><svg><use href="#i-mail"/></svg>darren@kolvistylaw.com</li>
    <li>2150 Harbor Point Dr. Suite 410</li>
    <li>Bayview Ranch, Florida 34299</li>
  </ul>
  <div class="band"></div>
  <div class="web"><svg><use href="#i-web"/></svg>kolvistylaw.com</div>
</section>

<section class="sheet card c4">
  <span class="mark"></span>
  <div class="firm">Darren Kolvisty, P.A.</div>
  <div class="tagline">Personal Injury Attorneys</div>
</section>

<section class="sheet card c5">
  <div class="head"><div class="name">Darren Kolvisty</div><div class="role">Attorney at Law</div></div>
  <div class="line"></div>
  <ul class="contact">
    <li><svg><use href="#i-phone"/></svg>941.555.0182</li>
    <li><svg><use href="#i-fax"/></svg>941.555.0147</li>
    <li class="gap"></li>
    <li><svg><use href="#i-mail"/></svg>darren@kolvistylaw.com</li>
    <li><svg><use href="#i-web"/></svg>kolvistylaw.com</li>
    <li class="gap"></li>
    <li>2150 Harbor Point Drive Suite 410</li>
    <li>Bayview Ranch, Florida 34299</li>
  </ul>
  <span class="mark"></span>
</section>

<section class="sheet card c6">
  <div class="ghost-name">Kolvisty</div>
  <div class="head"><div class="name">Darren Kolvisty</div><div class="role">Attorney at Law</div></div>
  <div class="line"></div>
  <ul class="contact">
    <li><svg><use href="#i-phone"/></svg>941.555.0182</li>
    <li><svg><use href="#i-fax"/></svg>941.555.0147</li>
    <li class="gap"></li>
    <li><svg><use href="#i-mail"/></svg>darren@kolvistylaw.com</li>
    <li><svg><use href="#i-web"/></svg>kolvistylaw.com</li>
    <li class="gap"></li>
    <li>2150 Harbor Point Drive Suite 410</li>
    <li>Bayview Ranch, Florida 34299</li>
  </ul>
</section>

<section class="sheet envelope e1">
  <div class="ghost-name">Kolvisty</div>
  <div class="brand">
    <span class="mark"></span>
    <div><div class="firm">Darren Kolvisty, P.A.</div><div class="tagline">Personal Injury Attorneys</div></div>
  </div>
  <ul class="contact">
    <li><svg><use href="#i-mail"/></svg>darren@kolvistylaw.com</li>
    <li><svg><use href="#i-web"/></svg>kolvistylaw.com</li>
    <li>2150 Harbor Point Drive Suite 410</li>
    <li>Bayview Ranch, Florida 34299</li>
  </ul>
</section>

<section class="sheet envelope e2">
  <svg class="flap" viewBox="0 0 349 40" aria-hidden="true">
    <path d="M0 14 Q20 16 40 30 L160 36 Q174 38 188 36 L309 30 Q329 16 349 14" fill="none" stroke="#b8b8b8" stroke-width="1"/>
  </svg>
  <span class="mark"></span>
</section>
</body>
</html>
```